Dailyvane Homepare Redesign - Morris

After scores of designs were submitted in response to our recent PixelGuild competition to re-think the Dailyvane.com homepage, we went back and looked at each of the artist’s portfolios. Several - including yours - were of particular interest to you.
We are now asking a handful of these designers to take a stab at a new Dailyvane.com homepage – again – but this time in accordance with some fresh guidelines. (See below.)
For this you will be paid $500 (US). We would need to have your work by Friday, March 4.
Furthermore, if we ask you to take your design through several additional stages, to a “final,” you will be paid an additional $750.
Please let us know as soon as possible if you are agreeable to this proposal.
What we have attached here are several wireframes that will help guide you to what we are after.
There are two wireframes, the first is that of the homepage. It has an area, at the top, that we are calling “the canvas”. The canvas will display different templates. The second wireframe features four different canvas templates.
We would like you to design one main homepage comp.
Once you are done with the homepage comp, please create 4 versions of it, each with a different canvas template in the “canvas” area.
Remember, the wireframes are for position only. Please use your creative judgment on colors, sizes, scale, styles, and graphics.
Generally speaking, it should be apparent that we seek a spare, clean look – easy to navigate, not too crowded with small images or unnecessary embellishment. Our audience tends to be older and not especially Web-savvy.
If you have any questions, do not hesitate to ask.
Will you participate in this project?

```html
<!DOCTYPE html>
<html lang="en">
<head>
<meta charset="utf-8">
<title>Dailyvane.com — Homepage</title>
<link href="https://fonts.googleapis.com/css2?family=Arimo:wght@400;700&display=swap" rel="stylesheet">
<style>
:root{
  --black:#000;
  --red:#e8180c;
  --red-dark:#c40f05;
  --blue:#1c8fcd;
  --blue-light:#4fb9ec;
  --blue-text:#0a72c0;
  --head-blue:#1e8fd0;
  --frame:#e3e6ea;
  --text:#222;
  --muted:#555;
}
*{box-sizing:border-box;margin:0;padding:0}
html,body{width:1200px;height:900px;overflow:hidden;background:#fff;font-family:"Arimo",Arial,sans-serif;color:var(--text)}
body{position:relative}
.abs{position:absolute}
a{color:inherit}

.topbar{left:0;top:0;width:1200px;height:46px;background:var(--black)}
.topbar span{position:absolute;top:11px;height:22px;line-height:22px;color:#fff;font-weight:700;font-size:12.5px}
.topbar .active{background:var(--red);border-radius:3px;width:71px;text-align:center}

.header{left:0;top:46px;width:1200px;height:147px;background:linear-gradient(#f4f4f4,#d9d9d9)}
.logo{left:105px;top:78px;font-size:45px;font-weight:700;color:var(--head-blue);letter-spacing:-1px;line-height:52px;white-space:nowrap}
.tagline{left:323px;top:133px;font-size:12px;font-weight:700;color:#222}
.pipe{left:466px;top:96px;font-size:13px;color:#333}
.account{left:490px;top:90px;font-size:12px;white-space:nowrap}
.account a{color:var(--blue-text);font-weight:700}
.account .welcome{font-size:11px;color:#111;margin-top:3px}
.hot{left:683px;top:77px;font-size:11px;white-space:nowrap}
.hot strong{color:var(--red);display:block;margin-bottom:3px}
.hot span{color:#333}
.hot i{font-style:normal;color:#aaa;margin:0 5px}
.search{left:684px;top:111px;width:411px;height:25px;display:flex}
.search .field{flex:1;border:2px solid var(--red);border-right:none;background:#fff;font-size:11px;color:#555;padding:4px 9px}
.search .btn{width:63px;background:linear-gradient(#f2483d,var(--red-dark));color:#fff;font-size:11px;font-weight:700;text-align:center;line-height:25px;border-radius:0 3px 3px 0}

.mainnav{left:105px;top:156px;width:990px;height:38px;background:linear-gradient(var(--blue-light),var(--blue));border-radius:5px 5px 0 0;display:flex}
.mainnav span{height:38px;line-height:38px;text-align:center;color:#fff;font-weight:700;font-size:12.5px;border-right:1px solid #7ccbf0;white-space:nowrap}
.mainnav .current{background:linear-gradient(#f25a4f,var(--red));border-radius:5px 5px 0 0;height:42px;margin-top:-4px;line-height:42px;border:none}
.mainnav span:last-child{border:none;text-align:left}

.mustreads{left:0;top:194px;width:1200px;height:36px;background:linear-gradient(#fafafa,#e6e6e6);border-bottom:2px solid #ececec;font-size:11.5px;font-weight:700;line-height:36px;padding-left:119px;white-space:nowrap}
.mustreads b{color:#0b5f9a;font-size:12px;margin-right:8px}
.mustreads span{padding:0 10px;border-left:1px solid #ccc}
.mustreads span:first-of-type{border:none;padding-left:0}

.feature{left:105px;top:242px;width:990px;height:453px;background:var(--frame);padding:7px}
.feature .inner{width:976px;height:439px;background:#fff;position:relative}
.feature h1{position:absolute;left:0;top:16px;width:976px;text-align:center;color:var(--head-blue);font-size:35.5px;font-weight:700;letter-spacing:-.3px;white-space:nowrap}
.feature .photo{position:absolute;left:157px;top:61px;width:662px;height:265px;background:linear-gradient(135deg,#1c2148,#4a4d78 45%,#2b2b3c 75%,#6b5850)}
.arrow{position:absolute;top:346px;width:26px;height:78px;background:linear-gradient(90deg,#f2483d,var(--red-dark))}
.arrow svg{position:absolute;left:8px;top:33px}
.thumb{position:absolute;top:346px;height:78px;background:linear-gradient(#fff,#e8eaec);text-align:center;font-size:11px;color:var(--blue-text);line-height:13px}
.thumb .pic{width:82px;height:32px;margin:6px auto 8px;background:linear-gradient(135deg,#2b3a8a,#6b7ac8 50%,#3a3f66);border:1px solid #ccc}
.thumb span{text-decoration:underline}
.thumb.on{background:var(--blue);color:#fff}
.thumb.on span{text-decoration:none}
.thumb.on::before{content:"";position:absolute;left:42px;top:-8px;border:9px solid transparent;border-top:none;border-bottom-color:var(--blue)}

.newsfront{left:105px;top:708px;width:677px;height:192px;background:var(--frame);padding:7px 7px 0;overflow:hidden}
.newsfront .inner{background:#fff;height:185px;overflow:hidden}
.newsfront h2{height:40px;line-height:40px;padding-left:14px;color:#fff;font-size:18px;background:linear-gradient(var(--blue-light),var(--blue))}
.story{position:relative;height:91px;margin:0 14px;border-bottom:1px dotted #999}
.story .pic{position:absolute;left:2px;top:17px;width:73px;height:59px;background:linear-gradient(#6b6e78,#3a3530)}
.story h3{position:absolute;left:88px;top:21px;font-size:14px;letter-spacing:-.25px;color:var(--blue-text);white-space:nowrap}
.story p{position:absolute;left:88px;top:40px;width:545px;font-size:12px;line-height:18px;color:var(--muted)}

.alerts{left:795px;top:708px;width:300px;height:179px;background:linear-gradient(#f43a2c,var(--red-dark));border:5px solid #e01c10;outline:1px solid #b50c04}
.alerts h2{position:absolute;left:55px;top:14px;color:#fff;font-size:19px;font-weight:700;white-space:nowrap}
.alerts svg{position:absolute;left:13px;top:16px}
.alerts label{position:absolute;color:#fff;font-weight:700;font-size:11px;width:50px;text-align:right;left:0}
.alerts .field{position:absolute;left:59px;width:213px;height:25px;background:#fff;border:1px solid #900;font-size:11px;line-height:23px;padding-left:10px;color:#222}
.alerts .go{position:absolute;left:70px;top:128px;width:72px;height:24px;border-radius:3px;background:linear-gradient(#fff,#d6d6d6);border:1px solid #888;font-size:12px;font-weight:700;text-align:center;line-height:22px;color:#111}
</style>
</head>
<body>

<nav class="topbar abs">
  <span class="active" style="left:105px">MONEY</span>
  <span style="left:210px">HEALTH</span>
  <span style="left:303px">WORLD</span>
  <span style="left:398px">TV</span>
  <span style="left:462px">VOICES</span>
</nav>

<header class="header abs"></header>
<div class="logo abs">Dailyvane.com</div>
<div class="tagline abs">Your Tagline Here</div>
<div class="pipe abs">|</div>
<div class="account abs"><a href="#">Sign In</a> <span style="color:#999">|</span> <a href="#">Register</a><div class="welcome">Welcome to Dailyvane</div></div>
<div class="hot abs"><strong>Hot Topics:</strong><span>Lorem</span><i>|</i><span>Lipsum</span><i>|</i><span>Quisque</span><i>|</i><span>Vestibulum</span><i>|</i><span>Mauris</span></div>
<div class="search abs"><div class="field">Enter Your Keword</div><div class="btn">SEARCH</div></div>

<nav class="mainnav abs">
  <span class="current" style="width:100px">NewsFront</span>
  <span style="width:117px">United States</span>
  <span style="width:83px">Politics</span>
  <span style="width:92px">The Wire</span>
  <span style="width:80px">Voices</span>
  <span style="width:118px">Fast Features</span>
  <span style="width:106px">Technology</span>
  <span style="width:105px">Slideshows</span>
  <span style="width:76px">Jokes</span>
  <span style="flex:1">Cartoons</span>
</nav>

<div class="mustreads abs">
  <b>Must Reads:</b>
  <span>Lorem ipsum dolor sit amet</span><span>Nullam molestie ligula eni</span><span>Vestibulum vel vestibulum tellus</span><span>Integer lacinia erat vel sapien commodo</span>
</div>

<section class="feature abs">
  <div class="inner">
    <h1>Vestibulu vestibulum tellus uisque tempor commodo.</h1>
    <div class="photo" role="img" aria-label="Lead story photo: a speaker at a rally holding a microphone"></div>
    <div class="arrow" style="left:15px"><svg width="10" height="12"><path d="M9 0v12L0 6z" fill="#fff"/></svg></div>
    <div class="arrow" style="left:935px"><svg width="10" height="12"><path d="M0 0v12l10-6z" fill="#fff"/></svg></div>
    <div class="thumb" style="left:47px;width:108px"><div class="pic" role="img" aria-label="Story thumbnail"></div><span>Volutpat ante in<br>erat</span></div>
    <div class="thumb on" style="left:158px;width:104px"><div class="pic" role="img" aria-label="Story thumbnail"></div><span>Vestibulu veste-<br>inthinh telles</span></div>
    <div class="thumb" style="left:265px;width:108px"><div class="pic" role="img" aria-label="Story thumbnail"></div><span>Cras convallis<br>tellus</span></div>
    <div class="thumb" style="left:376px;width:108px"><div class="pic" role="img" aria-label="Story thumbnail"></div><span>Vivamus pul<br>vinarpurus eg</span></div>
    <div class="thumb" style="left:487px;width:108px"><div class="pic" role="img" aria-label="Story thumbnail"></div><span>Vivamus pul<br>vinarpurus eg</span></div>
    <div class="thumb" style="left:598px;width:108px"><div class="pic" role="img" aria-label="Story thumbnail"></div><span>Cras convallis<br>tellus</span></div>
    <div class="thumb" style="left:709px;width:108px"><div class="pic" role="img" aria-label="Story thumbnail"></div><span>Vivamus pul<br>vinarpurus eg</span></div>
    <div class="thumb" style="left:820px;width:108px"><div class="pic" role="img" aria-label="Story thumbnail"></div><span>Vivamus pul<br>vinarpurus eg</span></div>
  </div>
</section>

<section class="newsfront abs">
  <div class="inner">
    <h2>NewsFront</h2>
    <article class="story">
      <div class="pic" role="img" aria-label="Story photo of a speaker"></div>
      <h3>Vestibulu vestibulum tellus that hasining the bashing uisque teipor ancommodo.</h3>
      <p>Vestibulum vehicula hendrerit interdum. Pellentesque id leo quis erat posuere tempor anthat anec nisanDuis mattis iaculis eros et convallis. Nullam molestie ligula enimel condimentum...</p>
    </article>
    <article class="story" style="border:none">
      <div class="pic" role="img" aria-label="Story photo of a speaker"></div>
      <h3>Vestibulu vestibulum tellus that hasining the bashing uisque teipor ancommodo.</h3>
      <p>Vestibulum vehicula hendrerit interdum. Pellentesque id leo quis erat posuere tempor anthat anec</p>
    </article>
  </div>
</section>

<aside class="alerts abs">
  <svg width="32" height="22" viewBox="0 0 32 22"><rect x="1" y="1" width="30" height="20" fill="#f7c600" stroke="#b88a00"/><path d="M1 1l15 11L31 1" fill="none" stroke="#b88a00" stroke-width="1.5"/></svg>
  <h2>Sign up for News Alerts</h2>
  <label style="top:63px">Email:</label>
  <div class="field" style="top:52px">Enter Your Email ID</div>
  <label style="top:97px">Zip:</label>
  <div class="field" style="top:87px">Enter Your ZIP Code</div>
  <div class="go">Sign Up</div>
</aside>

</body>
</html>
```